One page website for a Personal Injury Law Firm

Design and code a one page website in WordPress for the Darrow Law Firm, which is a a personal injury law firm located in Coral Gables, Florida. Please note: if you want to change the color pallete for the logo and for the web design , that is fine by me.

Target Market(s)

Those injured in accidents that need legal representation

Industry/Entity Type

Legal

Coding

Coded - Design and coding required

Number of Pages Required

1 page

Font styles to use
Other font styles liked:
• Montserrat

```html
<!DOCTYPE html>
<html lang="en">
<head>
<meta charset="utf-8">
<title>Darrow Law Firm | Personal Injury Attorneys</title>
<link href="https://fonts.googleapis.com/css2?family=Cormorant+Garamond:wght@500;600;700&family=Montserrat:wght@400;500;600;700&display=swap" rel="stylesheet">
<style>
:root{
  --navy:#1e2a45;
  --navy-deep:#141d33;
  --gold:#c49a5e;
  --gold-light:#dcbf8f;
  --beige:#f6efe6;
  --paper:#ffffff;
  --mist:#f2f2f4;
  --ink:#1d2233;
  --muted:#5e6474;
  --serif:'Cormorant Garamond', Georgia, serif;
  --sans:'Montserrat', Arial, sans-serif;
}
*{margin:0;padding:0;box-sizing:border-box}
html,body{width:1200px;height:4384px;overflow:hidden}
body{font-family:var(--sans);color:var(--ink);background:var(--paper);position:relative}
section,header,footer{position:relative;width:1200px;overflow:hidden}
.btn{display:inline-block;background:var(--gold);color:#fff;font:600 12px var(--sans);padding:11px 24px;border-radius:2px;text-decoration:none}

/* Brand mark: name with a plain square */
.brand{display:flex;align-items:center;gap:10px}
.brand-square{width:14px;height:14px;background:var(--gold)}
.brand-name{font:600 16px var(--sans);color:#fff;letter-spacing:.5px;white-space:nowrap}

/* Hero */
.hero{height:600px;background:linear-gradient(180deg,#4a3a2c 0%,#3a2c22 45%,#1f1a18 100%)}
.hero-photo{position:absolute;inset:0;background:radial-gradient(ellipse at 50% 45%,#7a6048 0%,#4b3a2c 45%,#221b17 100%);opacity:.9}
.hero-shade{position:absolute;inset:0;background:linear-gradient(180deg,rgba(20,29,51,.25) 0%,rgba(20,29,51,.1) 50%,rgba(20,29,51,.75) 100%)}
.topbar{position:absolute;top:8px;right:40px;display:flex;gap:24px;font-size:10px;color:#e9e3da}
.topbar span{display:flex;align-items:center;gap:6px}
.hero .brand{position:absolute;left:40px;top:36px}
.nav{position:absolute;top:32px;right:40px;display:flex;align-items:center;gap:30px;font-size:12px;font-weight:500;color:#fff}
.nav .active{background:var(--gold);padding:8px 14px}
.nav .btn{padding:9px 16px;font-size:11px}
.hero-copy{position:absolute;left:0;right:0;top:388px;text-align:center;color:#fff}
.hero-copy h1{font:700 46px var(--serif);letter-spacing:1px}
.hero-copy p{font-size:14px;font-weight:500;margin-top:6px;color:#f1e7d8}
.hero-copy .btn{margin-top:30px}

/* About */
.about{height:560px;background:var(--paper)}
.about-ghost{position:absolute;left:14px;top:110px;writing-mode:vertical-rl;transform:rotate(180deg);font:700 84px var(--sans);color:#f1eee9;letter-spacing:6px;line-height:1}
.about-copy{position:absolute;left:120px;top:48px;width:440px}
.about-copy h2{font:700 34px var(--serif);line-height:1.15;color:var(--navy)}
.about-copy p{font-size:11px;line-height:1.75;color:var(--muted);margin-top:18px}
.about-copy .btn{margin-top:24px}
.about-frame{position:absolute;left:610px;top:38px;width:470px;height:350px;border:2px solid var(--gold)}
.about-photo{position:absolute;left:596px;top:24px;width:470px;height:350px;background:linear-gradient(135deg,#d9d4cc 0%,#8b8176 45%,#2d3142 100%)}

/* Consultation bar */
.consult{height:140px}
.consult-bar{position:absolute;left:200px;top:24px;width:800px;height:80px;background:var(--navy);border:1px solid var(--gold);outline:4px solid var(--navy);display:flex;align-items:center;padding:0 32px;gap:40px;color:#fff}
.consult-bar h3{font:600 26px var(--serif)}
.consult-item{display:flex;align-items:center;gap:10px;font-size:11px;padding-left:20px;border-left:1px solid rgba(255,255,255,.25)}
.consult-item small{display:block;color:var(--gold-light);font-size:10px}

/* Why */
.why{height:440px;background:var(--mist)}
.why h2{text-align:center;margin-top:96px;font:700 36px var(--serif);color:var(--navy)}
.why .sub{text-align:center;font-size:13px;font-weight:600;margin-top:6px}
.why-feature{position:absolute;width:260px}
.why-feature h4{font-size:13px;font-weight:700;color:var(--navy)}
.why-feature p{font-size:10px;line-height:1.7;color:var(--muted);margin-top:6px}
.why-emblem{position:absolute;left:560px;top:250px;width:80px;height:80px;border-radius:50%;background:var(--navy);border:3px solid var(--gold)}

/* Examples */
.examples{height:620px;background:var(--beige)}
.examples-ghost{position:absolute;left:0;right:0;top:70px;text-align:center;font:700 92px var(--sans);color:rgba(196,154,94,.14);letter-spacing:6px}
.examples h2{text-align:center;margin-top:108px;font:700 36px var(--serif);color:var(--navy);position:relative}
.examples .sub{text-align:center;font-size:13px;font-weight:600;margin-top:6px;position:relative}
.case{position:absolute;left:200px;width:800px;background:#fff;border-left:3px solid var(--gold);padding:22px 28px;font-size:11px;line-height:1.7;color:var(--muted);box-shadow:0 2px 10px rgba(0,0,0,.05)}

/* Strategy */
.strategy{height:280px;background:var(--navy);color:#fff}
.strategy h2{text-align:center;margin-top:36px;font:600 36px var(--serif);line-height:1.15}
.pillars{position:absolute;left:110px;right:110px;top:150px;display:flex;gap:20px}
.pillar{flex:1;background:rgba(255,255,255,.05);border:1px solid rgba(255,255,255,.1);padding:16px 18px}
.pillar .ico{width:34px;height:34px;background:var(--gold);display:flex;align-items:center;justify-content:center;margin-bottom:8px}
.pillar h4{font-size:13px;font-weight:700}
.pillar p{font-size:10px;line-height:1.6;color:#c7cbd6;margin-top:4px}

/* Practice */
.practice{height:460px;background:#fff}
.practice h2{position:absolute;left:120px;top:36px;font:700 36px var(--serif);color:var(--navy)}
.practice .sub{position:absolute;left:120px;top:82px;font-size:13px;font-weight:600}
.arrows{position:absolute;right:40px;top:50px;display:flex;gap:8px}
.arrows span{width:30px;height:30px;background:var(--gold);display:flex;align-items:center;justify-content:center}
.arrows span.dim{background:#b9a37f}
.pa-photo{position:absolute;top:160px;height:230px}
.pa-card{position:absolute;top:160px;height:230px;background:#fff;border:1px solid #e6e2dc;padding:26px 22px}
.pa-card h3{font:600 30px var(--serif);color:var(--navy);line-height:1.1}
.pa-card p{font-size:10px;line-height:1.7;color:var(--muted);margin-top:12px}

/* Florida law */
.law{height:560px;background:#fff}
.law-panel{position:absolute;left:860px;top:0;width:340px;height:560px;background:var(--navy)}
.law-ghost{position:absolute;left:1130px;top:150px;writing-mode:vertical-rl;transform:rotate(180deg);font:700 64px var(--sans);color:rgba(255,255,255,.07);letter-spacing:4px;line-height:1}
.law-photo{position:absolute;left:720px;top:80px;width:400px;height:480px;background:linear-gradient(180deg,#2a3350 0%,#3b4563 40%,#1a2037 100%)}
.law h2{position:absolute;left:120px;top:40px;font:700 40px var(--serif);line-height:1.1;color:var(--navy)}
.law .sub{position:absolute;left:120px;top:140px;font-size:12px;font-weight:600}
.law-item{position:absolute;left:120px;width:600px;background:#f3f3f5;padding:22px 24px 22px 92px}
.law-item .ico{position:absolute;left:26px;top:22px;width:44px;height:44px;border-radius:50%;background:var(--navy);display:flex;align-items:center;justify-content:center}
.law-item h4{font-size:13px;font-weight:700;color:var(--navy)}
.law-item p{font-size:10px;line-height:1.65;color:var(--muted);margin-top:6px}

/* CTA */
.cta{height:240px;background:linear-gradient(180deg,#2d3550 0%,#1c2440 100%);color:#fff;text-align:center}
.cta h2{margin-top:34px;font:600 38px var(--serif)}
.cta .sub{font-size:13px;font-weight:600;margin-top:6px;color:var(--gold-light)}
.cta p{font-size:10px;color:#c2c7d4;margin:16px auto 0;width:560px;line-height:1.6}
.cta .btn{margin-top:16px}

/* Footer */
.footer{height:484px;background:var(--navy-deep);color:#fff;text-align:center}
.footer .brand{position:absolute;left:0;right:0;top:50px;justify-content:center}
.footer .brand-name{font-size:20px}
.footer .brand-square{width:18px;height:18px}
.footer h3{position:absolute;left:0;right:0;top:112px;font:600 20px var(--serif)}
.footer .tag{position:absolute;left:0;right:0;top:146px;font-size:10px;color:var(--gold-light)}
.footer-nav{position:absolute;left:0;right:0;top:222px;display:flex;justify-content:center;gap:110px;font-size:11px}
.footer-rule{position:absolute;left:80px;right:80px;height:1px;background:rgba(255,255,255,.15)}
.footer-contacts{position:absolute;left:80px;right:80px;top:290px;display:flex;justify-content:space-between;text-align:left;font-size:11px}
.footer-contacts div{display:flex;align-items:center;gap:10px}
.footer-contacts small{display:block;color:var(--gold-light);font-size:10px}
.fico{width:34px;height:34px;background:var(--gold);display:flex;align-items:center;justify-content:center}
.copyright{position:absolute;left:0;right:0;top:440px;font-size:10px;color:#9aa0b2}
</style>
</head>
<body>

<header class="hero">
  <div class="hero-photo" role="img" aria-label="Attorney in a suit seated at a conference table in a wood-panelled office"></div>
  <div class="hero-shade"></div>
  <div class="brand"><span class="brand-square"></span><span class="brand-name">Darrow Law Firm</span></div>
  <div class="topbar">
    <span><svg width="10" height="10" viewBox="0 0 24 24"><path fill="#c49a5e" d="M6.6 10.8a15 15 0 0 0 6.6 6.6l2.2-2.2c.3-.3.7-.4 1-.2 1.1.4 2.3.6 3.6.6.6 0 1 .4 1 1V20c0 .6-.4 1-1 1A17 17 0 0 1 3 4c0-.6.4-1 1-1h3.5c.6 0 1 .4 1 1 0 1.3.2 2.5.6 3.6.1.3 0 .7-.2 1z"/></svg>(305) 555-0147</span>
    <span><svg width="10" height="10" viewBox="0 0 24 24"><path fill="#c49a5e" d="M2 5h20v14H2zm2 2v.5l8 5 8-5V7z"/></svg>hello@darrowlegal.com</span>
  </div>
  <nav class="nav">
    <span class="active">Home</span><span>About</span><span>Practice Areas ▾</span><span>Testimonials</span><span>Blog</span><span class="btn">Contact Us</span>
  </nav>
  <div class="hero-copy">
    <h1>THE DARROW LAW FIRM</h1>
    <p>Concierge-Level Personal Injury Representation In Miami, Florida</p>
    <span class="btn">Get Started</span>
  </div>
</header>

<section class="about">
  <div class="about-ghost">ABOUT US</div>
  <div class="about-copy">
    <h2>Justice. Recovery. A Better<br>Future Starts Here.</h2>
    <p>At The Darrow Law Firm, we understand that suffering a personal injury can be life-altering, physically, emotionally and financially. You may be unsure whether pursuing legal action is the right step. But in Florida, holding negligent parties accountable isn't just your right, it's often necessary to rebuild your life.</p>
    <p>We take a concierge-level approach to personal injury law, offering personalized attention, strategic advocacy, and relentless dedication to securing the maximum compensation you deserve. Our mission is not only to make you whole again but to help you build a brighter future, ensuring access to the best medical care, financial stability and peace of mind for you and your loved ones.</p>
    <span class="btn">Learn More</span>
  </div>
  <div class="about-frame"></div>
  <div class="about-photo" role="img" aria-label="Three attorneys meeting with a client around an office table"></div>
</section>

<section class="consult">
  <div class="consult-bar">
    <h3>Free Consultation:</h3>
    <div class="consult-item"><svg width="18" height="18" viewBox="0 0 24 24"><path fill="#c49a5e" d="M6.6 10.8a15 15 0 0 0 6.6 6.6l2.2-2.2c.3-.3.7-.4 1-.2 1.1.4 2.3.6 3.6.6.6 0 1 .4 1 1V20c0 .6-.4 1-1 1A17 17 0 0 1 3 4c0-.6.4-1 1-1h3.5c.6 0 1 .4 1 1 0 1.3.2 2.5.6 3.6.1.3 0 .7-.2 1z"/></svg><span><small>Call Us</small>(305) 555-0147</span></div>
    <div class="consult-item"><svg width="18" height="18" viewBox="0 0 24 24"><path fill="#c49a5e" d="M2 5h20v14H2zm2 2v.5l8 5 8-5V7z"/></svg><span><small>Mail Us</small>hello@darrowlegal.com</span></div>
  </div>
</section>

<section class="why">
  <h2>Why Choose The Darrow Law Firm?</h2>
  <p class="sub">Unmatched Experience. Proven Results. Relentless Advocacy.</p>
  <svg style="position:absolute;left:0;top:0" width="1200" height="440"><path d="M400 290 H540 M660 290 H800 M600 332 V360" stroke="#c49a5e" stroke-width="1" fill="none" stroke-dasharray="4 4"/></svg>
  <div class="why-feature" style="left:120px;top:262px"><h4>25+ Years of Legal Mastery</h4><p>We have successfully handled thousands of cases, fighting tirelessly for injured Floridians. Our proven trial experience gives us an insider advantage in every case we take on.</p></div>
  <div class="why-emblem"></div>
  <div class="why-feature" style="left:820px;top:262px"><h4>Extensive Knowledge of Insurance Tactics</h4><p>Having worked for insurance companies, we know their strategies, loopholes, and how to dismantle their defenses to maximize your settlement.</p></div>
  <div class="why-feature" style="left:470px;top:366px;width:260px;text-align:center"><h4>Millions Recovered for Clients</h4><p>Our track record includes life-changing results.</p></div>
</section>

<section class="examples">
  <div class="examples-ghost">EXAMPLES</div>
  <h2>How We Fight For Our Clients' Futures</h2>
  <p class="sub">These Are Just A Few Examples Of How We Fight For Our Clients' Futures—Not Just Their Cases.</p>
  <div class="case" style="top:210px">A client left partially paralyzed after a major spinal injury received specialized rehabilitation care. We secured compensation that covered all medical bills, paid off their home, and funded their children's college education.</div>
  <div class="case" style="top:318px">A client suffered a severe infection from a minor slip-and-fall injury at a Miami condo building. We resolved the case before filing a lawsuit, securing funds that allowed him to buy a new home, pay off debts, and provide private school tuition for his children.</div>
  <div class="case" style="top:426px">A fatal truck accident in Naples impacted a family's future. Beyond proving the company at fault, we fought for financial stability. We secured a settlement that covered private-school tuition, housing costs for the spouse, and her daughter's college tuition.</div>
</section>

<section class="strategy">
  <h2>Our Strategy: Aggressive, Client-Focused,<br>and Results-Driven</h2>
  <div class="pillars">
    <div class="pillar"><div class="ico"><svg width="18" height="18" viewBox="0 0 24 24"><path fill="#fff" d="M3 21h18v-2H3zm2-4h3v-7H5zm5.5 0h3v-7h-3zM16 17h3v-7h-3zM12 2 2 7v2h20V7z"/></svg></div><h4>Taking On Corporate Giants</h4><p>We don't back down from big insurance companies or large corporate firms.</p></div>
    <div class="pillar"><div class="ico"><svg width="18" height="18" viewBox="0 0 24 24"><path fill="#fff" d="M12 12a4 4 0 1 0 0-8 4 4 0 0 0 0 8zm0 2c-4 0-8 2-8 5v2h16v-2c0-3-4-5-8-5z"/></svg></div><h4>Concierge-Style Legal Care</h4><p>You're not just a case number. We provide dedicated, personal guidance.</p></div>
    <div class="pillar"><div class="ico"><svg width="18" height="18" viewBox="0 0 24 24"><path fill="none" stroke="#fff" stroke-width="2.5" d="M5 12l5 5 9-10"/></svg></div><h4>No Win, No Fee Guarantee</h4><p>We take your case on a contingency basis, you only pay if we win.</p></div>
  </div>
</section>

<section class="practice">
  <h2>Our Practice Areas</h2>
  <p class="sub">Comprehensive Representation For The Injured</p>
  <div class="arrows">
    <span class="dim"><svg width="12" height="12" viewBox="0 0 24 24"><path d="M15 4 7 12l8 8" stroke="#fff" stroke-width="3" fill="none"/></svg></span>
    <span><svg width="12" height="12" viewBox="0 0 24 24"><path d="M9 4l8 8-8 8" stroke="#fff" stroke-width="3" fill="none"/></svg></span>
  </div>
  <div class="pa-photo" style="left:0;width:300px;background:linear-gradient(135deg,#9aa0a8,#4c525c)" role="img" aria-label="Damaged cars after a collision"></div>
  <div class="pa-card" style="left:300px;width:300px"><h3>Car Accidents</h3><p>We fight for victims of rear-end crashes, multi-vehicle collisions, pedestrian and cyclist accidents, and more.</p></div>
  <div class="pa-photo" style="left:610px;width:300px;background:linear-gradient(135deg,#c9c6c1,#77716b)" role="img" aria-label="Person who has fallen on a wet floor"></div>
  <div class="pa-card" style="left:910px;width:290px"><h3>Slip and Fall /<br>Premises Liability</h3><p>If you were injured due to unsafe conditions at a business, hotel, condo, or public space, we hold negligent property owners accountable.</p></div>
</section>

<section class="law">
  <div class="law-panel"></div>
  <div class="law-photo" role="img" aria-label="Two attorneys in suits standing side by side"></div>
  <div class="law-ghost">PROTECTIONS</div>
  <h2>Florida Personal Injury Law:<br>What You Need To Know</h2>
  <p class="sub">Your Rights And Legal Protections</p>
  <div class="law-item" style="top:190px"><div class="ico"><svg width="20" height="20" viewBox="0 0 24 24"><path fill="#c49a5e" d="M12 3 4 7v2h16V7zM6 11v7h2v-7zm5 0v7h2v-7zm5 0v7h2v-7zM4 20v2h16v-2z"/></svg></div><h4>Comparative Negligence (Florida Statutes §768.81)</h4><p>We don't need a liability percentage set by a jury, we build your case so that you get all our clients a guarantee that if we don't win, you don't pay.</p></div>
  <div class="law-item" style="top:310px"><div class="ico"><svg width="20" height="20" viewBox="0 0 24 24"><circle cx="12" cy="12" r="8" stroke="#c49a5e" stroke-width="2" fill="none"/><path d="M12 7v5l3 2" stroke="#c49a5e" stroke-width="2" fill="none"/></svg></div><h4>Statute Of Limitations (Florida Statutes §95.11)</h4><p>You have two years to file a personal injury claim and four years for wrongful death cases. Missing these deadlines can prevent you from recovering compensation.</p></div>
  <div class="law-item" style="top:430px"><div class="ico"><svg width="20" height="20" viewBox="0 0 24 24"><path fill="#c49a5e" d="M12 3 3 10h3v10h12V10h3z"/></svg></div><h4>Premises Liability (Florida Statutes §768.0755)</h4><p>Property owners are responsible for dangerous conditions that harm or should have known about.</p></div>
</section>

<section class="cta">
  <h2>Take The First Step Toward Justice</h2>
  <p class="sub">Let Us Fight For The Compensation You Deserve</p>
  <p>If you have been injured due to someone else's negligence, do not wait. Time-sensitive deadlines could impact your case.</p>
  <span class="btn">Get A Consultation</span>
</section>

<footer class="footer">
  <div class="brand"><span class="brand-square"></span><span class="brand-name">Darrow Law Firm</span></div>
  <h3>The Darrow Law Firm: Where Justice Meets Dedication.</h3>
  <p class="tag">Free Consultation | No Fees Unless We Win | Aggressive Representation</p>
  <div class="footer-rule" style="top:200px"></div>
  <div class="footer-nav"><span>Home</span><span>About</span><span>Practice Areas</span><span>Testimonials</span><span>Blog</span><span>Contact Us</span></div>
  <div class="footer-rule" style="top:262px"></div>
  <div class="footer-contacts">
    <div><span class="fico"><svg width="14" height="14" viewBox="0 0 24 24"><path fill="#fff" d="M12 2a7 7 0 0 0-7 7c0 5 7 13 7 13s7-8 7-13a7 7 0 0 0-7-7zm0 9.5A2.5 2.5 0 1 1 12 6.5a2.5 2.5 0 0 1 0 5z"/></svg></span><span><small>Visit Us</small>1420 Alcazar Way, Coral Gables, FL 33134</span></div>
    <div><span class="fico"><svg width="14" height="14" viewBox="0 0 24 24"><path fill="#fff" d="M6.6 10.8a15 15 0 0 0 6.6 6.6l2.2-2.2c.3-.3.7-.4 1-.2 1.1.4 2.3.6 3.6.6.6 0 1 .4 1 1V20c0 .6-.4 1-1 1A17 17 0 0 1 3 4c0-.6.4-1 1-1h3.5c.6 0 1 .4 1 1 0 1.3.2 2.5.6 3.6.1.3 0 .7-.2 1z"/></svg></span><span><small>Call Us</small>(305) 555-0147</span></div>
    <div><span class="fico"><svg width="14" height="14" viewBox="0 0 24 24"><path fill="#fff" d="M2 5h20v14H2zm2 2v.5l8 5 8-5V7z"/></svg></span><span><small>Mail Us</small>hello@darrowlegal.com</span></div>
  </div>
  <div class="footer-rule" style="top:410px"></div>
  <p class="copyright">© 2025 Darrow Law Firm. All Rights Reserved.</p>
</footer>

</body>
</html>
```